Harborline Capital Advisors
New Business Card
Project: Harborline Capital Advisors
Harborline Capital Advisors - Financial Services
Creative Brief
Professional
Gavin R. Marsh
Partner
1875 Corporate Drive Ste 210 PO Box 8627 San Ramon, CA 94583
gavin.marsh@qbn-mail.com
www.harborlinecapitaladvisors.com
CA Insurance License #3K91604
Gavin Marsh is a registered representative of Granton Fiscal Counsel Corp. Harborline Capital Advisors, an independent firm. Securities offered through Granton Fiscal Counsel Corp., a broker-dealer (member NVBA). Investment advisory services offered through Trelford Advisory, a division of Granton Fiscal Counsel Corp., a registered investment advisor. Insurance offered through Granton Outreach and Insurance Agency, LLC and Granton Allied Insurance Agency, Inc. and other fine companies.
GavinMarsh7316 GavinMarsh7316
Show me some solid black cards
I would definitely want to see all the required disclosures and a front and back design. Thanks!

```html
<!DOCTYPE html>
<html lang="en">
<head>
<meta charset="utf-8">
<title>Harborline Capital Advisors – Stationery Set</title>
<link rel="stylesheet" href="https://fonts.googleapis.com/css2?family=Cinzel:wght@500&family=Open+Sans:wght@400;600&display=swap">
<style>
:root{
  --bg:#e7e8ea;
  --paper:#ffffff;
  --ink:#0b0b0e;
  --text:#3a3a40;
  --muted:#6c6d74;
  --card-text:#c9cbd3;
  --blue:#3b52c9;
  --blue-light:#7a8ff0;
}
*{box-sizing:border-box;margin:0;padding:0}
html,body{width:1200px;height:937px;overflow:hidden}
body{background:var(--bg);font-family:"Open Sans",sans-serif;color:var(--text);position:relative}
.sheet{position:absolute;background:var(--paper);overflow:hidden}
.wave{position:absolute;left:0;bottom:0;width:100%;display:block}
.brand{display:flex;flex-direction:column;align-items:center;gap:4px}
.brand-dot{width:14px;height:14px;border-radius:50%;background:var(--blue)}
.brand-name{font-family:"Cinzel",serif;font-weight:500;color:var(--ink);text-transform:uppercase;letter-spacing:.06em;text-align:center;line-height:1.15}
.web{position:absolute;color:var(--paper);font-family:"Open Sans",sans-serif;letter-spacing:.12em}

/* Letterhead */
.letterhead{left:182px;top:68px;width:388px;height:544px}
.letterhead .brand{position:absolute;left:30px;top:36px}
.letterhead .brand-name{font-size:11px;width:120px}
.letterhead .contact{position:absolute;right:24px;top:34px;font-size:5.5px;line-height:1.5;text-align:right;width:140px;color:var(--muted)}
.letterhead .body{position:absolute;left:30px;top:118px;width:320px;font-size:5.6px;line-height:1.65}
.letterhead .body p{margin-bottom:8px}
.letterhead .signature{width:34px;height:16px;margin:4px 0 6px;background:linear-gradient(90deg,#c9cad0,#9d9ea6)}
.letterhead .wave{height:92px}

/* Folder */
.folder{left:633px;top:38px;width:463px;height:574px}
.folder .brand{position:absolute;left:0;right:0;top:196px}
.folder .brand-dot{width:26px;height:26px}
.folder .brand-name{font-size:24px;width:300px}
.folder .wave{height:112px}
.folder .web{left:22px;bottom:18px;font-size:10px}

/* Business cards – solid black */
.card{width:200px;height:104px;left:40px;background:var(--ink)}
.card-front{top:650px}
.card-back{top:770px}
.card .brand-name{color:var(--paper)}
.card-front .brand{position:absolute;left:10px;top:16px}
.card-front .brand-dot{width:9px;height:9px}
.card-front .brand-name{font-size:6.5px;width:70px}
.card-front .details{position:absolute;left:92px;top:12px;width:104px;font-size:4.6px;line-height:1.5;color:var(--card-text)}
.card-front .details strong{display:block;font-size:6.4px;color:var(--paper);font-weight:600}
.card-front .details .role{display:block;margin-bottom:3px;color:var(--blue-light)}
.card-back .brand{position:absolute;left:0;right:0;top:9px;gap:3px}
.card-back .brand-dot{width:9px;height:9px}
.card-back .brand-name{font-size:7px;width:170px}
.card .accent{position:absolute;left:0;width:100%;display:block}
.card-front .accent{bottom:0;height:22px}
.card-back .accent{top:40px;height:8px}
.card-back .disclosure{position:absolute;left:9px;right:9px;top:50px;font-size:4.3px;line-height:1.4;color:var(--card-text);text-align:justify}

/* Envelopes */
.envelope-front{left:266px;top:668px;width:433px;height:205px}
.envelope-front .brand{position:absolute;left:30px;top:20px}
.envelope-front .brand-dot{width:13px;height:13px}
.envelope-front .brand-name{font-size:10px;width:120px}
.envelope-front .wave{height:82px}
.envelope-front .web{left:20px;bottom:12px;font-size:7.5px}
.envelope-back{left:739px;top:668px;width:426px;height:205px}
.envelope-back .flap{position:absolute;left:0;top:0;width:100%;height:92px;display:block}
.envelope-back .web{left:0;right:0;top:30px;text-align:center;font-size:10px}
</style>
</head>
<body>

<section class="sheet letterhead" aria-label="Letterhead">
  <div class="brand"><span class="brand-dot"></span><span class="brand-name">Harborline Capital Advisors</span></div>
  <address class="contact">1875 Corporate Drive Ste 210<br>PO Box 8627<br>San Ramon, CA 94583<br>gavin.marsh@qbn-mail.com<br>www.harborlinecapitaladvisors.com</address>
  <div class="body">
    <p>July 3, 2019</p>
    <p>Alan Reed<br>1200 Main Street, Suite 12<br>Dublin, CA 94568</p>
    <p>Thank you for the time you spent with us this week. We value the chance to review your goals and to outline a plan that fits your needs for growth, income and long term security.</p>
    <p>Please find the summary enclosed. We will call next week to set a follow up meeting at a time that suits you.</p>
    <p>Our team remains ready to answer any questions about your accounts, your coverage or the steps ahead in the plan we discussed together.</p>
    <p>Best regards,</p>
    <div class="signature" role="img" aria-label="Handwritten signature"></div>
    <p>Gavin R. Marsh<br>Partner<br>1875 Corporate Drive Ste 210, San Ramon, CA 94583</p>
  </div>
  <svg class="wave" viewBox="0 0 400 100" preserveAspectRatio="none" aria-hidden="true">
    <path d="M0 48 C120 100 260 30 400 6 L400 12 C260 36 120 106 0 54Z" fill="var(--blue-light)"/>
    <path d="M0 56 C120 108 260 38 400 16 L400 28 C260 48 120 116 0 66Z" fill="var(--blue)"/>
    <path d="M0 68 C120 118 260 50 400 30 L400 100 L0 100Z" fill="var(--ink)"/>
  </svg>
</section>

<section class="sheet folder" aria-label="Presentation folder">
  <div class="brand"><span class="brand-dot"></span><span class="brand-name">Harborline Capital Advisors</span></div>
  <svg class="wave" viewBox="0 0 400 100" preserveAspectRatio="none" aria-hidden="true">
    <path d="M0 34 C130 90 270 24 400 4 L400 10 C270 30 130 96 0 40Z" fill="var(--blue-light)"/>
    <path d="M0 42 C130 98 270 32 400 14 L400 26 C270 42 130 106 0 52Z" fill="var(--blue)"/>
    <path d="M0 54 C130 108 270 44 400 28 L400 100 L0 100Z" fill="var(--ink)"/>
  </svg>
  <span class="web">www.harborlinecapitaladvisors.com</span>
</section>

<section class="sheet card card-front" aria-label="Business card front">
  <div class="brand"><span class="brand-dot"></span><span class="brand-name">Harborline Capital Advisors</span></div>
  <div class="details">
    <strong>Gavin R. Marsh</strong>
    <span class="role">Partner</span>
    1875 Corporate Drive Ste 210<br>PO Box 8627, San Ramon, CA 94583<br>gavin.marsh@qbn-mail.com<br>www.harborlinecapitaladvisors.com<br>CA Insurance License #3K91604
  </div>
  <svg class="accent" viewBox="0 0 400 100" preserveAspectRatio="none" aria-hidden="true">
    <path d="M0 60 C120 110 260 40 400 10 L400 30 C260 60 120 130 0 80Z" fill="var(--blue)"/>
  </svg>
</section>

<section class="sheet card card-back" aria-label="Business card back">
  <div class="brand"><span class="brand-dot"></span><span class="brand-name">Harborline Capital Advisors</span></div>
  <svg class="accent" viewBox="0 0 400 20" preserveAspectRatio="none" aria-hidden="true">
    <path d="M0 8 C130 20 270 0 400 8 L400 12 C270 4 130 24 0 12Z" fill="var(--blue)"/>
  </svg>
  <p class="disclosure">Gavin Marsh is a registered representative of Granton Fiscal Counsel Corp. Harborline Capital Advisors, an independent firm. Securities offered through Granton Fiscal Counsel Corp., a broker-dealer (member NVBA). Investment advisory services offered through Trelford Advisory, a division of Granton Fiscal Counsel Corp., a registered investment advisor. Insurance offered through Granton Outreach and Insurance Agency, LLC and Granton Allied Insurance Agency, Inc. and other fine companies.</p>
</section>

<section class="sheet envelope-front" aria-label="Envelope front">
  <div class="brand"><span class="brand-dot"></span><span class="brand-name">Harborline Capital Advisors</span></div>
  <svg class="wave" viewBox="0 0 400 100" preserveAspectRatio="none" aria-hidden="true">
    <path d="M0 40 C130 96 270 28 400 4 L400 10 C270 34 130 102 0 46Z" fill="var(--blue-light)"/>
    <path d="M0 48 C130 104 270 36 400 14 L400 26 C270 46 130 112 0 58Z" fill="var(--blue)"/>
    <path d="M0 60 C130 114 270 48 400 28 L400 100 L0 100Z" fill="var(--ink)"/>
  </svg>
  <span class="web">www.harborlinecapitaladvisors.com</span>
</section>

<section class="sheet envelope-back" aria-label="Envelope back">
  <svg class="flap" viewBox="0 0 400 100" preserveAspectRatio="none" aria-hidden="true">
    <path d="M0 0 H400 V70 C300 96 100 96 0 70Z" fill="var(--ink)"/>
    <path d="M0 70 C100 96 300 96 400 70 L400 76 C300 102 100 102 0 76Z" fill="var(--blue)"/>
  </svg>
  <span class="web">www.harborlinecapitaladvisors.com</span>
</section>

</body>
</html>
```